Webdesign/ Redesign of community frontpage (only design, no code!)

Our social community website (http://www.tavro.eu) needs a fresh, more invitating frontpage. Our audience are 14 - 25 year old.

Only the screen design (psd & image) is needed, no code (no html, no css, ...).

Style:
- Modern/ clear/ lightweight/ invitating design for young people
- Emphasize the intent of the website (social community website, meeting other young people to chat, hangout, ..)
- Optimized for 1024x768

Elements that must appear:
- Logo (attached as EPS, can be modified if needed)
- Login form (Username, Password, Status/Feeling, Forgot password link, ...)
- Link to registration page OR registration form
- Empty space (around 350x250 pixel) where a video or other dynamic content could be embedded (done by myself)
- Five feature/pro statements (max. 60 letters each, not necessarily to be displayed as a group, see below)
- Currently present links in footer
- Some statistics (Number of people online, total number of members (females/ males))

Elements that might appear:
- Registration form instead of link to separate registration form (ex like chatterloop has it)

Ideas:
- Registration form could also be designed to be a layer that'll show when the user clicks
- If the design needs/allows it, I can also animate random member photos (80x80 pixels) and place them on the frontpage using js/ ajax

Feature/pro statements examples (see above):
- Dauerhaft kostenlos für Frauen und Männer
- Reale Profile, extrem wenig Fakes & Störenfriede
- Persönliches Profil mit vielen Funktionen
- Hoher Schutz deiner Privatsphäre und Daten
- Viele freundliche Mitarbeiter und Helfer
Updates

After having reviewed the first two designs, I'd like to give these general ideas/ feedback:

1. I think it would be much better to _not_ have the whole registration form on the frontpage but instead only a link which opens the form in a layer/dialog when clicked. Of course only the design of the dialog needs to be done, I'll do the actual coding. To have a first impression of how the dialog could look like, please see the newly attached dialog.png (the text in the dialog is just for demo and should be replaced by the actual registration form).

2. There should be no separation between males/ females like it is currently. I think it'd better to mix because it emphasizes the community/ group character of the site and does not make it look too much like da dating site.

3. I think the five statements/ pros I mentioned (why should people register, what are the greatest features of our site, ..) could be best displayed as balloon tips (just like in comics) next to some images of users.

4. The color of the site should not be too heavy and should make people feel comfortable.

5. The logo provied must be fixed to read "TAVRO.eu" instead of "LUNEK.de". I hope this i no big deal, sorry for that. This could also be done afterwards for a small additional amount of money, as it doesn't really affect the overall design.

To better illustrate all my writings above I just made two simple sketches and attached them (frontpage.png and frontpage_with_active_registration.png).

Important: these only show all the elements that must appear on the page and what I thought might be a good idea of how to present the pros/ features of my site. The actual placements, sizes, arragements etc. can of course all be different.

Looking forward to your create additions and design skills to make this look pretty... :-)

Just to emphasize, the design should not look or feel heavy. So please keep the colors light/ soft, no huge images, don't stretch the logo to much, etc.

Please do not insert any content (like search boxes, text blocks, etc.) which is not already present in my mockups. The only thing that should be additionally added is a link/ button so people can login using openid (chatterloop, wexplore, ..) too.

Target Market(s)

Young people 14 - 25 years old interested in meeting friends, new people, chat, flirt, hangout, have fun.

Industry/Entity Type

Community

Requirements
Must have
• see description
Nice to have
• see description
Should not have
• plugin dependencies (ex flash)

```html
<!DOCTYPE html>
<html lang="en">
<head>
<meta charset="utf-8">
<title>TAVRO.eu – chat, flirt &amp; more</title>
<link href="https://fonts.googleapis.com/css2?family=Arimo:wght@400;700&family=PT+Sans:wght@700&display=swap" rel="stylesheet">
<style>
  :root{
    --canvas-top:#ececec;
    --canvas-bottom:#d7d8d8;
    --lime-top:#f7ef25;
    --lime-bottom:#a6cd3b;
    --stage-top:#cbcbcb;
    --stage-mid:#a8a9a9;
    --stage-bottom:#9fa0a0;
    --footer-top:#737476;
    --footer-bottom:#2d2e32;
    --bubble-top:#5a5b5e;
    --bubble-bottom:#1f2023;
    --label:#6e6c47;
    --ink:#111;
    --white:#fff;
    --accent:#b3d53a;
    --stats-top:#c3df4c;
    --stats-bottom:#8fbf2f;
  }
  *{box-sizing:border-box;margin:0;padding:0}
  html,body{width:1200px;height:961px;overflow:hidden}
  body{
    position:relative;
    font-family:"Arimo",Arial,sans-serif;
    background:linear-gradient(var(--canvas-top),var(--canvas-bottom));
  }
  .page{position:absolute;left:89px;top:86px;width:1012px;height:759px;box-shadow:0 0 3px rgba(0,0,0,.15)}
  .site-header{
    position:absolute;left:0;top:0;width:1012px;height:125px;
    background:linear-gradient(var(--lime-top) 0%,var(--lime-top) 55%,var(--lime-bottom) 100%);
    border:1px solid #c9d94a;
  }
  .brand{position:absolute;left:39px;top:14px;color:var(--ink)}
  .brand-name{font-weight:700;font-size:46px;letter-spacing:2px;line-height:1}
  .brand-tagline{font-weight:700;font-size:21px;letter-spacing:1px;margin-top:4px}
  .brand-intro{font-size:8px;color:#555;margin-top:4px;font-weight:700}

  .login{position:absolute;left:0;top:0;width:1012px;height:125px;font-size:9px;font-weight:700}
  .login label{position:absolute;color:var(--label)}
  .field{position:absolute;width:109px;height:19px;background:var(--white);border:1px solid #d9e08a;border-radius:5px}
  .lbl-user{left:674px;top:33px}
  .lbl-pass{left:674px;top:64px}
  .in-user{left:724px;top:28px}
  .in-pass{left:724px;top:60px}
  .remember{position:absolute;left:724px;top:89px;display:flex;align-items:center;gap:7px;color:var(--label)}
  .remember .box{width:11px;height:11px;background:var(--white);border:1px solid #999}
  .status{position:absolute;left:868px;top:28px;width:109px;height:19px;background:var(--white);border-radius:4px;display:flex;align-items:center;overflow:hidden;color:#333}
  .status span{flex:1;text-align:center}
  .status .arrow{width:17px;height:19px;background:#3a3b3e;display:flex;align-items:center;justify-content:center}
  .btn-login{position:absolute;left:867px;top:61px;width:110px;height:19px;border-radius:4px;border:none;
    background:linear-gradient(#6b6c70,#2a2b2f);color:var(--white);font:700 9px "Arimo",Arial,sans-serif}
  .forgot{position:absolute;right:36px;top:91px;color:var(--label);text-decoration:none}

  .stage{
    position:absolute;left:0;top:125px;width:1012px;height:537px;
    background:linear-gradient(var(--stage-top) 0%,#bdbdbd 30%,var(--stage-mid) 32%,var(--stage-bottom) 100%);
  }
  .member{position:absolute;width:80px;height:80px;border:4px solid var(--white);border-radius:8px;box-shadow:0 1px 3px rgba(0,0,0,.3)}
  .bubble{position:absolute;width:154px;height:53px;border-radius:8px;padding:10px 10px 0 9px;
    background:linear-gradient(var(--bubble-top),var(--bubble-bottom) 55%,#3c3d40);
    border:1px solid #777;color:var(--white);font-size:9.5px;font-weight:700;line-height:1.3;box-shadow:0 1px 3px rgba(0,0,0,.3)}
  .bubble::after{content:"";position:absolute;left:12px;bottom:-10px;width:8px;height:10px;background:#2a2b2e;border-radius:0 0 4px 4px}
  .bubble-signup{width:213px;height:74px;padding:8px 0 0 15px;font-size:14px;line-height:1.3}
  .bubble-signup .lead{font-size:15px}
  .bubble-signup .signup{color:var(--accent);font-size:17px;text-decoration:none;display:block;line-height:1.1}
  .bubble-signup::after{left:18px}

  .stats{position:absolute;left:43px;top:413px;width:190px;height:91px;border-radius:10px;
    background:linear-gradient(var(--stats-top),var(--stats-bottom));border:2px solid #d7ea8b;
    color:var(--white);font-size:18px;font-weight:700;padding:20px 0 0 22px;line-height:1.3;letter-spacing:-.5px}

  .media{position:absolute;left:651px;top:285px;width:256px;height:192px;background:#111;border-radius:7px}
  .media-screen{position:absolute;left:7px;top:8px;width:243px;height:173px;
    background:radial-gradient(circle at 40% 35%,#f3eaa0,#c9a23c 45%,#6e4a1c 80%,#3a2814)}
  .media-badge{position:absolute;left:-6px;top:11px;width:134px;height:36px;background:linear-gradient(#e9f03a,#a7cd3a);
    border:1px solid #c7d84a;font-weight:700;font-size:20px;letter-spacing:1px;color:var(--ink);display:flex;align-items:center;padding-left:16px}
  .media-play{position:absolute;left:36px;top:156px;width:35px;height:21px;background:linear-gradient(#555,#222);border:1px solid #888;border-radius:2px;display:flex;align-items:center;justify-content:center}
  .media-bar{position:absolute;left:77px;top:158px;width:143px;height:16px;background:linear-gradient(#555,#222);border:1px solid #888;border-radius:2px}
  .media-bar i{position:absolute;left:4px;top:5px;width:98px;height:5px;background:#bbb;border-radius:2px}
  .media-caption{position:absolute;left:650px;top:488px;width:280px;font-family:"PT Sans",Arial,sans-serif;font-weight:700;font-size:11px;color:var(--white);line-height:1.3}

  .site-footer{position:absolute;left:0;top:662px;width:1012px;height:65px;
    background:linear-gradient(var(--footer-top),#4c4d50 40%,var(--footer-bottom));color:var(--white);font-size:8.5px}
  .footer-links{position:absolute;left:39px;top:34px;list-style:none;display:flex}
  .footer-links li+li::before{content:"|";margin:0 5px}
  .footer-links a{color:var(--white);text-decoration:none}
  .copyright{position:absolute;right:36px;top:33px;font-weight:700}
  .footer-band{position:absolute;left:0;top:727px;width:1012px;height:32px;background:linear-gradient(var(--lime-top),var(--lime-bottom))}
</style>
</head>
<body>
<div class="page">
  <header class="site-header">
    <div class="brand">
      <div class="brand-name">TAVRO.eu</div>
      <div class="brand-tagline">chat, flirt &amp; more</div>
      <p class="brand-intro">TAVRO helps you connect and share with the people in your life.</p>
    </div>
    <form class="login">
      <label class="lbl-user">Username</label>
      <span class="field in-user"></span>
      <label class="lbl-pass">Password</label>
      <span class="field in-pass"></span>
      <div class="remember"><span class="box"><svg width="11" height="11" viewBox="0 0 11 11"><path d="M2 5.5l2.5 2.5L9 2" stroke="#222" stroke-width="1.6" fill="none"/></svg></span>Remember me</div>
      <div class="status"><span>Status - Feeling</span><span class="arrow"><svg width="9" height="7" viewBox="0 0 9 7"><path d="M0 0h9L4.5 7z" fill="#fff"/></svg></span></div>
      <button class="btn-login" type="button">Login</button>
      <a class="forgot" href="#">Forgot Password?</a>
    </form>
  </header>

  <main class="stage">
    <div class="member" style="left:47px;top:71px;background:linear-gradient(135deg,#ddd,#777)" role="img" aria-label="Member photo"></div>
    <div class="member" style="left:266px;top:69px;background:linear-gradient(135deg,#d9b39a,#8a5f46)" role="img" aria-label="Member photo"></div>
    <div class="member" style="left:466px;top:70px;background:linear-gradient(135deg,#e8d2b8,#b4866a)" role="img" aria-label="Member photo"></div>
    <div class="member" style="left:688px;top:54px;background:linear-gradient(135deg,#8f6f5e,#3a2a24)" role="img" aria-label="Member photo"></div>
    <div class="member" style="left:855px;top:61px;background:linear-gradient(135deg,#e6c6b2,#a07e6c)" role="img" aria-label="Member photo"></div>
    <div class="member" style="left:132px;top:167px;background:linear-gradient(135deg,#c8966e,#2b6a6a)" role="img" aria-label="Member photo"></div>
    <div class="member" style="left:369px;top:162px;background:linear-gradient(135deg,#e0c394,#6b4a3a)" role="img" aria-label="Member photo"></div>
    <div class="member" style="left:662px;top:172px;background:linear-gradient(135deg,#d6e2ea,#b08c8c)" role="img" aria-label="Member photo"></div>
    <div class="member" style="left:829px;top:185px;background:linear-gradient(135deg,#bfb8a8,#6f7061)" role="img" aria-label="Member photo"></div>
    <div class="member" style="left:508px;top:201px;background:linear-gradient(135deg,#a8442a,#3a1a12)" role="img" aria-label="Member photo"></div>
    <div class="member" style="left:75px;top:302px;background:linear-gradient(135deg,#f0f0f0,#666)" role="img" aria-label="Member photo"></div>
    <div class="member" style="left:318px;top:277px;background:linear-gradient(135deg,#b98a6a,#4a3328)" role="img" aria-label="Member photo"></div>
    <div class="member" style="left:498px;top:305px;background:linear-gradient(135deg,#f4eef0,#6a5a60)" role="img" aria-label="Member photo"></div>
    <div class="member" style="left:289px;top:427px;background:linear-gradient(135deg,#e6c08e,#9a6a3c)" role="img" aria-label="Member photo"></div>
    <div class="member" style="left:532px;top:420px;background:linear-gradient(135deg,#c68a6a,#5a2a1a)" role="img" aria-label="Member photo"></div>

    <div class="bubble bubble-signup" style="left:93px;top:20px">
      <div class="lead">No account yet?</div>
      <a class="signup" href="#">Sing up</a>
      <div>it’s free and always will be!</div>
    </div>
    <p class="bubble" style="left:517px;top:54px">It’s great to hang out, chat and make new friends!</p>
    <p class="bubble" style="left:558px;top:169px">So many great features, like webcam chat, image galleries, games...</p>
    <p class="bubble" style="left:363px;top:230px">I like it because it’s free for everyone!</p>
    <p class="bubble" style="left:124px;top:262px">It’s just the best community i know of! ;)</p>
    <p class="bubble" style="left:339px;top:391px;padding-left:15px">I like how they care of my</p>

    <div class="stats">89.433 Members<br>4.645 Online now</div>

    <div class="media">
      <div class="media-screen" role="img" aria-label="Video still of friends at a sunny party"></div>
      <div class="media-badge">TAVRO</div>
      <div class="media-play"><svg width="10" height="10" viewBox="0 0 10 10"><path d="M1 0l9 5-9 5z" fill="#fff"/></svg></div>
      <div class="media-bar"><i></i></div>
    </div>
    <p class="media-caption">Lorem Ipsum is simply dummy text of the printing and typesetting industry.</p>
  </main>

  <footer class="site-footer">
    <ul class="footer-links">
      <li><a href="#">Press Releases</a></li>
      <li><a href="#">Privacy Statement</a></li>
      <li><a href="#">Terms of Use</a></li>
      <li><a href="#">Jobs</a></li>
      <li><a href="#">Sitemap</a></li>
      <li><a href="#">Tell us what you think</a></li>
    </ul>
    <p class="copyright">Copyright 2010</p>
  </footer>
  <div class="footer-band"></div>
</div>
</body>
</html>
```